New wine label design needed for exciting new wine business

A wine label design is required for a new wine production business based in Australia. This label will need to incorporate the business name 'Oleno-Cru'. We would like it to have a classic feel for a super premium wine and to reflect prestige. Colour suggestions may include a white background and the use of the colour red although we are open to any colors. This label must reflect a serious wine at a serious price. We want our design to attract attention and have a relevance that will stand the test of time!

Thanks to everyone who provided designs for our wine label. We have been very impressed by the calibre of designs! We will be making a decision very soon.

```html
<!DOCTYPE html>
<html lang="en">
<head>
<meta charset="utf-8">
<title>Oleno-Cru Wine Label</title>
<link rel="stylesheet" href="https://fonts.googleapis.com/css2?family=Tinos&family=Parisienne&family=Source+Sans+3:wght@400&display=swap">
<style>
  :root {
    --page-bg: #ffffff;
    --label-black: #231f20;
    --label-white: #ffffff;
    --gold: #c9a93a;
    --red-deep: #a5121b;
    --red-bright: #e0202a;
    --ink: #2a2a2a;
    --note-ink: #231f20;
    --label-edge: #9a9a9a;
  }
  html, body {
    margin: 0;
    padding: 0;
    width: 1200px;
    height: 848px;
    overflow: hidden;
    background: var(--page-bg);
  }
  .canvas {
    position: relative;
    width: 1200px;
    height: 848px;
  }
  .colour-note {
    position: absolute;
    left: 20px;
    top: 320px;
    width: 102px;
    margin: 0;
    text-align: right;
    font-family: "Source Sans 3", Arial, sans-serif;
    font-size: 17px;
    line-height: 24px;
    color: var(--note-ink);
  }
  .wine-label {
    position: absolute;
    left: 166px;
    top: 200px;
    width: 344px;
    height: 432px;
    background: var(--label-white);
    border: 1px solid var(--label-edge);
    box-shadow: 6px 10px 10px rgba(0,0,0,0.35);
    display: flex;
    flex-direction: column;
  }
  .label-crown {
    height: 244px;
    background: var(--label-black);
    position: relative;
  }
  .brand-dot {
    position: absolute;
    left: 50%;
    top: 48px;
    width: 26px;
    height: 26px;
    margin-left: -13px;
    border-radius: 50%;
    background: var(--gold);
  }
  .brand-name {
    position: absolute;
    left: 0;
    right: 0;
    top: 112px;
    margin: 0;
    text-align: center;
    font-family: "Tinos", "Times New Roman", serif;
    font-weight: 400;
    font-size: 62px;
    line-height: 1;
    color: var(--gold);
  }
  .wine-type-band {
    height: 32px;
    background: linear-gradient(to right, var(--red-deep) 0%, var(--red-bright) 50%, var(--red-deep) 100%);
    display: flex;
    align-items: center;
    justify-content: center;
    font-family: "Tinos", "Times New Roman", serif;
    font-size: 19px;
    color: var(--ink);
  }
  .label-body {
    flex: 1;
    display: flex;
    flex-direction: column;
    align-items: center;
    justify-content: flex-end;
    padding-bottom: 14px;
  }
  .label-text {
    font-family: "Parisienne", cursive;
    font-size: 20px;
    color: var(--ink);
    margin: 0;
  }
  .volume {
    font-family: "Parisienne", cursive;
    font-size: 24px;
    color: var(--red-bright);
    margin: 2px 0 0;
  }
</style>
</head>
<body>
<main class="canvas">
  <p class="colour-note">OLENO-CRU &amp; grapes to be in gold color</p>

  <article class="wine-label">
    <header class="label-crown">
      <span class="brand-dot" aria-hidden="true"></span>
      <h1 class="brand-name">Oleno-Cru</h1>
    </header>
    <div class="wine-type-band">Quality Red Wine</div>
    <section class="label-body">
      <p class="label-text">Place your text here</p>
      <p class="volume">0,75 ml</p>
    </section>
  </article>
</main>
</body>
</html>
```